Korean Homemade food restaurant just like what your mom cooks at home

I need a black and white simple and modern design according to my logo.
My restaurant name is Nal Som (meaning of home cooking).
I need to have 늘찬(Nal Som) in Korean need to be included. Once again 늘찬.
I am not sure if I need to include my name and number and adress.
Updates

늘찬 Nal Som 478 Harwell Rd. Clarksville, TN 37118 Mark Yoon Owner Cell:931-608-2913 Store:931-617-3084

Target Market(s)

business owners, university students

Industry/Entity Type

Restaurant

Contact Information for Business Card

This is traditional Korean food restaurant that targets university students during lunch and Korean business travelers at dinner.

Font styles to use
Sans Serif

Requirements
Must have
• Must have my logo.

```html
<!DOCTYPE html>
<html lang="en">
<head>
<meta charset="utf-8">
<title>Nal Som — Business Card</title>
<link rel="stylesheet" href="https://fonts.googleapis.com/css2?family=Arimo:wght@400;700&family=Noto+Sans+KR:wght@400;700&display=swap">
<style>
  :root {
    --ink: #0b0b0b;
    --paper: #ffffff;
    --stage: #e9e6e2;
    --food-gold: #d9a552;
    --food-cream: #efd7a6;
    --food-green: #4f8a2e;
    --card-shadow: rgba(0, 0, 0, 0.18);
  }
  * { margin: 0; padding: 0; box-sizing: border-box; }
  html, body { width: 1200px; height: 848px; overflow: hidden; }
  body {
    background: var(--stage);
    font-family: "Arimo", "Noto Sans KR", Arial, sans-serif;
    color: var(--ink);
    display: flex;
    align-items: center;
    justify-content: center;
    gap: 40px;
  }
  .card {
    position: relative;
    width: 540px;
    height: 309px;
    background: var(--paper);
    box-shadow: 0 6px 18px var(--card-shadow);
    overflow: hidden;
  }
  .card-art { position: absolute; inset: 0; width: 100%; height: 100%; }

  .brand {
    position: absolute;
    display: flex;
    align-items: center;
    gap: 8px;
    font-weight: 700;
    letter-spacing: -0.5px;
    white-space: nowrap;
  }
  .brand-dot { background: var(--ink); border-radius: 50%; flex: none; }

  .card-front .brand { left: 306px; top: 44px; font-size: 26px; }
  .card-front .brand-dot { width: 12px; height: 12px; }

  .holder { position: absolute; left: 300px; top: 118px; width: 210px; text-align: center; }
  .holder-name { font-size: 28px; font-weight: 400; letter-spacing: -0.5px; white-space: nowrap; }
  .holder-role { font-size: 10px; margin-top: 2px; }

  .address {
    position: absolute;
    right: 18px; top: 214px;
    font-size: 11.5px;
    letter-spacing: -0.2px;
    white-space: nowrap;
  }
  .phone {
    position: absolute;
    display: flex;
    align-items: center;
    gap: 8px;
    color: var(--paper);
    font-size: 13px;
    white-space: nowrap;
  }
  .phone svg { width: 18px; height: 18px; flex: none; }
  .phone-store { right: 22px; top: 250px; }
  .phone-cell { left: 300px; top: 281px; }

  .card-back .brand {
    left: 50%; top: 50%;
    transform: translate(-50%, -50%);
    font-size: 56px;
    gap: 16px;
  }
  .card-back .brand-dot { width: 26px; height: 26px; }
</style>
</head>
<body>

  <section class="card card-front" aria-label="Business card front">
    <svg class="card-art" viewBox="0 0 540 309">
      <defs>
        <linearGradient id="food-tones" x1="0" y1="0" x2="1" y2="1">
          <stop offset="0" stop-color="#efd7a6"/>
          <stop offset="0.5" stop-color="#d9a552"/>
          <stop offset="1" stop-color="#4f8a2e"/>
        </linearGradient>
      </defs>
      <rect x="200" y="239" width="340" height="70" fill="#0b0b0b"/>
      <path d="M210 0 L262 0 C300 80 300 220 230 309 L150 309 C240 220 250 90 210 0 Z" fill="#0b0b0b"/>
      <path role="img" aria-label="Photo of crispy spring rolls on lettuce with chopsticks and porcelain plates"
            d="M0 0 L215 0 C255 90 245 220 155 309 L0 309 Z" fill="url(#food-tones)"/>
    </svg>

    <div class="brand"><span class="brand-dot"></span>늘찬 Nal Som</div>

    <div class="holder">
      <p class="holder-name">Mark Yoon</p>
      <p class="holder-role">Owner</p>
    </div>

    <p class="address">478 Harwell Rd. Clarksville, TN 37118</p>

    <p class="phone phone-store">
      <svg viewBox="0 0 18 18" aria-hidden="true">
        <rect width="18" height="18" rx="4" fill="#ffffff"/>
        <path d="M5.2 3.5 L7.3 3.5 L8 6.3 L6.7 7.4 C7.4 9 8.9 10.5 10.6 11.3 L11.7 10 L14.5 10.7 L14.5 12.8 C14.5 13.6 13.8 14.3 13 14.2 C8 13.6 4.4 10 3.8 5 C3.7 4.2 4.4 3.5 5.2 3.5 Z" fill="#0b0b0b"/>
      </svg>
      931-617-3084
    </p>

    <p class="phone phone-cell">
      <svg viewBox="0 0 18 18" aria-hidden="true">
        <rect width="18" height="18" rx="4" fill="#ffffff"/>
        <rect x="5.5" y="2.8" width="7" height="12.4" rx="1.4" fill="none" stroke="#0b0b0b" stroke-width="1.6"/>
        <rect x="7.8" y="12.6" width="2.4" height="0.9" fill="#0b0b0b"/>
      </svg>
      931-608-2913
    </p>
  </section>

  <section class="card card-back" aria-label="Business card back">
    <div class="brand"><span class="brand-dot"></span>늘찬 Nal Som</div>
  </section>

</body>
</html>
```